Harbor Ridge Holdings, LLC Business Card Design/Real Estate and Asset Mgmt.

Design business card with designer recommended colors using existing logo...teal color not mandatory. Business purpose is Asset Management and Real Estate.

The following text somewhere on the card:

HARBOR RIDGE HOLDINGS, LLC (llc can be very small font if needed.)
Owen Pelkey GRI, RRP, CHA, CHME (the abbreviations can be a smaller font)
PROPERTOR
517 Thornbury Lane #204-16
Crossville, TN 38555
Toll Free: 888-571-2934
Cell: 931.468.7325
Email: owenrpelkey@quillmail.example
www.harborridgeholdings.example

Target Market(s)

High net worth buyers and sellers. Will be providing commercial real estate sales and management services to banks and lenders who foreclose on bad debt collateral.

Industry/Entity Type

Real Estate

Contact Information for Business Card

Professional look. Maximum of two colors. Example: Logo one color and the text another. Or any combination the designer feels is appropriate.

Font styles to use
Other font styles liked:
• Designer's choice

Requirements
Must have
• Logo somewhere on the card.
Nice to have
• The card can be one sided or two sided or odd sized if the designer prefers.
• PROPERTOR Logo (small at the bottom or somewhere on the card. Even the back.)
Should not have
• Card should not be a folded card.

```html
<!DOCTYPE html>
<html lang="en">
<head>
<meta charset="utf-8">
<title>Harbor Ridge Holdings, LLC – Stationery</title>
<link rel="stylesheet" href="https://fonts.googleapis.com/css2?family=Cormorant+Garamond:wght@500;600&family=Open+Sans:wght@400;600&display=swap">
<style>
  :root{
    --teal:#1f9a9c;
    --teal-dark:#178588;
    --ink:#3a3a3a;
    --muted:#8a8a8a;
    --paper:#ffffff;
    --stage:#eef0f1;
    --shadow:rgba(0,0,0,.12);
  }
  *{box-sizing:border-box;margin:0;padding:0}
  html,body{width:1200px;height:746px;overflow:hidden;background:var(--stage)}
  .canvas{position:relative;width:1200px;height:746px}

  /* Letterhead */
  .letterhead{position:absolute;left:110px;top:36px;width:476px;height:674px;background:var(--paper);
    box-shadow:0 4px 18px var(--shadow);padding:44px 48px 0;font-family:"Open Sans",sans-serif;color:var(--ink)}
  .letterhead .brand{text-align:center;margin-bottom:40px}
  .brand-mark{display:inline-block;width:12px;height:12px;background:var(--teal);margin-bottom:6px}
  .brand-name{display:block;font-family:"Cormorant Garamond",serif;font-weight:600;color:var(--teal);
    font-size:13px;letter-spacing:2.5px}
  .letter{font-size:8.6px;line-height:1.55}
  .letter p{margin-bottom:10px}
  .letter .date{margin-bottom:2px}
  .signature{width:90px;height:26px;margin:6px 0 2px;background:linear-gradient(90deg,#e6e6e6,#f4f4f4)}
  .sign-title{font-weight:600}
  .letterhead .footer{position:absolute;left:0;right:0;bottom:0;height:44px;display:flex;align-items:center;
    padding:0 48px 0 0;font-size:7.4px;color:var(--muted)}
  .footer .tab{width:14px;height:10px;background:var(--teal);margin-right:34px}
  .footer span+span::before{content:"|";margin:0 6px}

  /* Cards */
  .card{position:absolute;width:350px;height:200px;box-shadow:0 4px 16px var(--shadow)}
  .card-back{left:680px;top:150px;background:var(--paper);padding:30px 28px;font-family:"Open Sans",sans-serif;color:var(--ink)}
  .card-front{left:680px;top:420px;background:var(--teal);display:flex;flex-direction:column;align-items:center;justify-content:center;color:#fff;text-align:center}
  .card-front .brand-mark{background:#fff;width:16px;height:16px;margin-bottom:12px}
  .card-front .brand-name{color:#fff;font-size:19px;letter-spacing:3px}
  .card-front .tagline{font-family:"Open Sans",sans-serif;font-size:7px;letter-spacing:1.5px;margin-top:6px;opacity:.9}

  .agent{display:flex;align-items:baseline;gap:8px}
  .agent-name{font-family:"Cormorant Garamond",serif;font-weight:600;font-size:22px;color:var(--teal)}
  .agent-creds{font-size:7px;color:var(--muted)}
  .agent-role{margin-left:auto;font-size:7px;font-weight:600;letter-spacing:1px}
  .card-back .company{margin-top:26px;font-family:"Cormorant Garamond",serif;font-weight:600;font-size:11px;letter-spacing:1.5px}
  .card-back .company small{font-size:7px}
  .address{font-size:7.4px;color:var(--muted);margin-top:3px}
  .contacts{list-style:none;margin-top:12px;font-size:7.4px;line-height:1.7}
  .contacts li{display:flex;align-items:center;gap:6px}
  .contacts svg{width:8px;height:8px;fill:var(--teal)}
  .card-back .tab{position:absolute;left:0;top:108px;width:6px;height:18px;background:var(--teal)}
</style>
</head>
<body>
<div class="canvas">

  <section class="letterhead">
    <header class="brand">
      <span class="brand-mark"></span>
      <span class="brand-name">HARBOR RIDGE HOLDINGS, LLC</span>
    </header>
    <div class="letter">
      <p class="date">November 1, 2015<br>Mr. Calvin Trent<br>88 Quarry Mill Lane<br>Fernvale, TN 38501</p>
      <p>Dear Mr. Trent,</p>
      <p>The first paragraph of a typical business letter states the main point of the letter. Begin with a friendly opening, then move quickly into the purpose of your letter. Use a couple of sentences to explain the purpose, but save the detail for the next paragraph.</p>
      <p>Beginning with the second paragraph, state the supporting details to justify your purpose. These may take the form of background information, statistics or first-hand accounts. A few short paragraphs within the body of the letter should be enough to support your reasoning and keep the reader engaged.</p>
      <p>Finally, in the closing paragraph, briefly restate your purpose and why it is important. If the purpose of your letter relates to your employment, consider ending with your contact information. Close with gratitude for the reader's time.</p>
      <p>Sincerely,</p>
      <div class="signature" role="img" aria-label="Handwritten signature of Walter Greaves"></div>
      <p class="sign-title">President</p>
    </div>
    <footer class="footer">
      <div class="tab"></div>
      <span>517 Thornbury Lane, Crossville TN 38555</span>
      <span>+1 888 571 2934</span>
      <span>info@harborridgeholdings.example</span>
      <span>www.harborridgeholdings.example</span>
    </footer>
  </section>

  <section class="card card-back">
    <div class="agent">
      <span class="agent-name">Owen Pelkey</span>
      <span class="agent-creds">GRI, RRP, CHA, CHME</span>
      <span class="agent-role">PROPERTOR</span>
    </div>
    <div class="tab"></div>
    <p class="company">HARBOR RIDGE HOLDINGS, <small>LLC</small></p>
    <p class="address">517 Thornbury Lane #204-16, Crossville, TN 38555</p>
    <ul class="contacts">
      <li><svg viewBox="0 0 10 10"><path d="M2 0h2l1 3-1.5 1a6 6 0 0 0 2.5 2.5L7 5l3 1v2c0 1-1 2-2 2A8 8 0 0 1 0 2c0-1 1-2 2-2z"/></svg>Toll Free: 888-571-2934</li>
      <li><svg viewBox="0 0 10 10"><rect x="2.5" y="0" width="5" height="10" rx="1"/></svg>Cell: 931.468.7325</li>
      <li><svg viewBox="0 0 10 10"><path d="M0 2h10v6H0z"/></svg>Email: owenrpelkey@quillmail.example</li>
      <li><svg viewBox="0 0 10 10"><circle cx="5" cy="5" r="5"/></svg>www.harborridgeholdings.example</li>
    </ul>
  </section>

  <section class="card card-front">
    <span class="brand-mark"></span>
    <span class="brand-name">HARBOR RIDGE HOLDINGS, LLC</span>
    <span class="tagline">ASSET MANAGEMENT &amp; REAL ESTATE</span>
  </section>

</div>
</body>
</html>
```